Business Card Design for Flood Rescue 360 - Property Restoration Professionals

I need a business card designed for Flood Rescue 360. We are a full-service property restoration solution. Providing water, fire, smoke & storm restoration as well as mold remediation and full remodel or reconstruction to homes and businesses across Dallas-Fort Worth, TX.
Target Market(s)
home and business owners with insurance covered property damage from water, fire or storm related damage
Industry/Entity Type
property restoration
Contact Information for Business Card
Martin Kell General Manager Cell: 214-555-0193 Office: 469-555-0148 email: Martin@FloodRescue360.example services: Water, Fire, Mold, Reconstruction Tagline: Fast Help When the Water Rises!
Look and feel
Each slider illustrates characteristics of the customer's brand and the style your logo design should communicate.

```html
<!DOCTYPE html>
<html lang="en">
<head>
<meta charset="utf-8">
<title>Flood Rescue 360 – Business Card</title>
<link href="https://fonts.googleapis.com/css2?family=Bebas+Neue&family=Roboto+Condensed:wght@700&family=Roboto:wght@400;500;700&display=swap" rel="stylesheet">
<style>
  :root {
    --stage: #ababab;
    --card: #ffffff;
    --blue: #0cb2e3;
    --grey: #7a7a7a;
    --text: #8c8c8c;
    --orange: #f0521f;
    --olive: #6b6a2e;
    --brown: #6a4a2a;
    --rule: #cfcfcf;
    --faint: #e3f6fb;
  }
  * { margin: 0; padding: 0; box-sizing: border-box; }
  html, body { width: 1200px; height: 1000px; overflow: hidden; }
  body { background: var(--stage); position: relative; font-family: "Roboto", sans-serif; }

  .card { position: absolute; left: 294px; width: 614px; height: 352px; background: var(--card); border-radius: 18px; overflow: hidden; box-shadow: 0 3px 6px rgba(0,0,0,0.25); }
  .card--front { top: 117px; }
  .card--back { top: 511px; }

  .brand { position: absolute; display: flex; align-items: center; gap: 14px; }
  .brand__name { font-family: "Roboto Condensed", sans-serif; font-weight: 700; color: var(--blue); text-transform: uppercase; line-height: 0.92; white-space: nowrap; }
  .brand__dot { border-radius: 50%; border: 6px solid var(--blue); flex: none; }

  .card--front .brand { left: 138px; top: 120px; }
  .card--front .brand__name { font-size: 50px; }
  .card--front .brand__dot { width: 92px; height: 92px; }

  .tagline { position: absolute; font-family: "Bebas Neue", sans-serif; color: var(--orange); letter-spacing: 1.6px; white-space: nowrap; }
  .card--front .tagline { left: 142px; top: 230px; font-size: 21px; letter-spacing: 2.2px; }

  .services { position: absolute; left: 140px; top: 261px; display: flex; align-items: center; gap: 6px; font-size: 14px; white-space: nowrap; }
  .services span { display: inline-flex; align-items: center; gap: 4px; }
  .svc-water { color: var(--blue); }
  .svc-fire { color: var(--orange); }
  .svc-mold { color: var(--olive); }
  .svc-build { color: var(--brown); }

  .card--back .brand { left: 39px; top: 47px; gap: 8px; }
  .card--back .brand__name { font-size: 27px; }
  .card--back .brand__dot { width: 52px; height: 52px; border-width: 4px; }
  .card--back .tagline { left: 41px; top: 110px; font-size: 11.5px; letter-spacing: 1px; }

  .watermark { position: absolute; left: 276px; top: -30px; width: 390px; height: 390px; border-radius: 50%; border: 3px solid var(--faint); }

  .person { position: absolute; left: 39px; top: 166px; }
  .person__name { font-size: 21px; font-weight: 700; letter-spacing: 0.5px; text-transform: uppercase; }
  .person__first { color: var(--blue); }
  .person__last { color: var(--grey); }
  .person__role { font-size: 12px; letter-spacing: 3px; color: var(--grey); text-transform: uppercase; margin-top: 3px; }
  .rule { position: absolute; left: 39px; top: 217px; width: 519px; height: 1px; background: var(--rule); }

  .address, .contact { position: absolute; left: 39px; font-size: 14px; line-height: 17px; color: var(--text); }
  .address { top: 226px; }
  .contact { top: 277px; }
  .contact b { color: var(--blue); font-weight: 700; }

  .icons { position: absolute; right: 53px; top: 280px; display: flex; gap: 18px; align-items: center; }
  .web { position: absolute; right: 54px; top: 313px; font-size: 14px; color: var(--text); }
  .web b { color: var(--blue); font-weight: 700; }
</style>
</head>
<body>

<section class="card card--front">
  <div class="brand">
    <div class="brand__name">Flood<br>Rescue 360</div>
    <div class="brand__dot"></div>
  </div>
  <p class="tagline">Fast help when the water rises!</p>
  <div class="services">
    <span class="svc-water"><svg width="11" height="16" viewBox="0 0 11 16"><path d="M5.5 0 C3 5 0 8 0 10.5 A5.5 5.5 0 0 0 11 10.5 C11 8 8 5 5.5 0Z" fill="var(--blue)"/></svg>WATER</span>
    <span class="svc-fire"><svg width="12" height="16" viewBox="0 0 12 16"><path d="M6 0 C7 4 12 6 11 11 A5 5 0 0 1 1 11 C0 8 3 7 3 4 C5 6 6 3 6 0Z" fill="var(--orange)"/></svg>FIRE</span>
    <span class="svc-mold"><svg width="15" height="15" viewBox="0 0 15 15" fill="var(--olive)"><circle cx="7.5" cy="2" r="1.6"/><circle cx="4" cy="5" r="1.6"/><circle cx="11" cy="5" r="1.6"/><circle cx="7.5" cy="7" r="1.6"/><circle cx="2.5" cy="9.5" r="1.6"/><circle cx="12.5" cy="9.5" r="1.6"/><circle cx="5.5" cy="11" r="1.6"/><circle cx="9.5" cy="11" r="1.6"/><circle cx="7.5" cy="13.5" r="1.4"/></svg>MOLD</span>
    <span class="svc-build"><svg width="15" height="15" viewBox="0 0 15 15" stroke="var(--brown)" stroke-width="2" stroke-linecap="round"><line x1="2" y1="14" x2="12" y2="4"/><line x1="13" y1="14" x2="3" y2="4"/><line x1="9" y1="1.5" x2="14" y2="6"/><line x1="1" y1="5" x2="6" y2="1.5"/></svg> RECONSTRUCTION</span>
  </div>
</section>

<section class="card card--back">
  <div class="watermark"></div>
  <div class="brand">
    <div class="brand__name">Flood<br>Rescue 360</div>
    <div class="brand__dot"></div>
  </div>
  <p class="tagline">Fast help when the water rises!</p>

  <div class="person">
    <h1 class="person__name"><span class="person__first">Martin</span> <span class="person__last">Kell</span></h1>
    <p class="person__role">General Manager</p>
  </div>
  <div class="rule"></div>

  <p class="address">4215 Lakeview Pkwy #210<br>Garland, TX 75044</p>
  <p class="contact"><b>C:</b> 214-555-0193<br><b>O:</b> 469-555-0148<br><b>E:</b> Martin@FloodRescue360.example</p>

  <div class="icons">
    <svg width="17" height="25" viewBox="0 0 11 16"><path d="M5.5 0 C3 5 0 8 0 10.5 A5.5 5.5 0 0 0 11 10.5 C11 8 8 5 5.5 0Z" fill="var(--blue)"/></svg>
    <svg width="18" height="25" viewBox="0 0 12 16"><path d="M6 0 C7 4 12 6 11 11 A5 5 0 0 1 1 11 C0 8 3 7 3 4 C5 6 6 3 6 0Z" fill="var(--orange)"/></svg>
    <svg width="23" height="23" viewBox="0 0 15 15" fill="var(--olive)"><circle cx="7.5" cy="2" r="1.6"/><circle cx="4" cy="5" r="1.6"/><circle cx="11" cy="5" r="1.6"/><circle cx="7.5" cy="7" r="1.6"/><circle cx="2.5" cy="9.5" r="1.6"/><circle cx="12.5" cy="9.5" r="1.6"/><circle cx="5.5" cy="11" r="1.6"/><circle cx="9.5" cy="11" r="1.6"/><circle cx="7.5" cy="13.5" r="1.4"/></svg>
    <svg width="22" height="22" viewBox="0 0 15 15" stroke="var(--brown)" stroke-width="2" stroke-linecap="round"><line x1="2" y1="14" x2="12" y2="4"/><line x1="13" y1="14" x2="3" y2="4"/><line x1="9" y1="1.5" x2="14" y2="6"/><line x1="1" y1="5" x2="6" y2="1.5"/></svg>
  </div>
  <p class="web"><b>FloodRescue360</b>.example</p>
</section>

</body>
</html>
```